Quorlan Visit cards serious but not sad

Hello, I'd like to design my visit cards with the logo Quorlan (attached) the following information: Name: Mathis Deloraux Title: Mobile Director: 33 (0) 6 28 40 13 85 Phone: 33 (0) 4 71 86 52 09 e-mail: mathis.deloraux@quorlan-advisory.example address: 17 Rue Anatole Berrin 92400 Courbevoie This visit will be used on the banking institutions and Quorlan is a consulting firm. I do not want to have dark background.

Target Market(s)

banks

Contact Information for Business Card

Name : Mathis Deloraux
Title : Director
mobile : +33(0)6 28 40 13 85
Phone : +33(0)4 71 86 52 09
e-mail: mathis.deloraux@quorlan-advisory.example
adresse : 17 Rue anatole Berrin 92400 Courbevoie

Requirements
Nice to have
• serious but not sad

```html
<!DOCTYPE html>
<html lang="en">
<head>
<meta charset="utf-8">
<title>Quorlan – Business Card</title>
<link rel="stylesheet" href="https://fonts.googleapis.com/css2?family=Russo+One&family=Roboto+Condensed:wght@400&display=swap">
<style>
  :root {
    --bg: #e6e8eb;
    --card-white: #f7f8f9;
    --brand-blue: #2a78c0;
    --band-light: #3a88c9;
    --band-dark: #0c58a6;
    --band-edge: #3b6fae;
    --text-light: #ffffff;
    --divider: rgba(255,255,255,0.35);
  }
  html, body {
    margin: 0;
    width: 1200px;
    height: 815px;
    overflow: hidden;
    background: var(--bg);
  }
  .stage {
    width: 1200px;
    height: 815px;
    display: flex;
    align-items: center;
    justify-content: center;
  }
  .card {
    position: relative;
    width: 900px;
    height: 560px;
    background: var(--card-white);
    overflow: hidden;
    box-shadow: 0 6px 24px rgba(0,0,0,0.12);
  }
  .card__brand {
    position: absolute;
    left: 56px;
    top: 72px;
    display: flex;
    align-items: center;
    gap: 18px;
  }
  .brand__dot {
    width: 112px;
    height: 112px;
    border-radius: 50%;
    background: var(--brand-blue);
  }
  .brand__name {
    font-family: "Russo One", sans-serif;
    font-size: 76px;
    line-height: 1;
    color: var(--brand-blue);
    letter-spacing: 1px;
  }
  .card__band {
    position: absolute;
    left: 0;
    right: 0;
    top: 250px;
    bottom: 0;
    background: linear-gradient(100deg, var(--band-light) 0%, var(--band-dark) 70%);
    border-top: 4px solid var(--band-edge);
  }
  .holder {
    position: absolute;
    left: 50px;
    top: 92px;
    color: var(--text-light);
  }
  .holder__name {
    font-family: "Russo One", sans-serif;
    font-size: 30px;
    margin: 0;
    font-weight: 400;
  }
  .holder__title {
    font-family: "Roboto Condensed", sans-serif;
    font-size: 20px;
    margin: 4px 0 0 6px;
  }
  .band__divider {
    position: absolute;
    left: 345px;
    top: 34px;
    width: 1px;
    height: 200px;
    background: var(--divider);
  }
  .contact {
    position: absolute;
    left: 378px;
    top: 38px;
    margin: 0;
    padding: 0;
    list-style: none;
    font-family: "Roboto Condensed", sans-serif;
    font-size: 20px;
    color: var(--text-light);
  }
  .contact__item {
    display: flex;
    align-items: center;
    gap: 14px;
    height: 36px;
  }
  .contact__icon {
    width: 14px;
    height: 14px;
    fill: var(--text-light);
    flex: none;
  }
  .band__dot {
    position: absolute;
    left: 555px;
    top: 200px;
    width: 6px;
    height: 6px;
    border-radius: 50%;
    background: var(--text-light);
  }
</style>
</head>
<body>
<main class="stage">
  <article class="card">
    <div class="card__brand">
      <span class="brand__dot"></span>
      <span class="brand__name">quorlan</span>
    </div>
    <section class="card__band">
      <div class="holder">
        <h1 class="holder__name">Mathis Deloraux</h1>
        <p class="holder__title">Director</p>
      </div>
      <span class="band__divider"></span>
      <ul class="contact">
        <li class="contact__item">
          <svg class="contact__icon" viewBox="0 0 14 14" aria-hidden="true"><path d="M7 0a5 5 0 0 0-5 5c0 3.6 5 9 5 9s5-5.4 5-9a5 5 0 0 0-5-5zm0 7a2 2 0 1 1 0-4 2 2 0 0 1 0 4z"/></svg>
          <span>17 Rue anatole Berrin 92400 Courbevoie</span>
        </li>
        <li class="contact__item">
          <svg class="contact__icon" viewBox="0 0 14 14" aria-hidden="true"><path d="M0 3h14v8H0z M0 3l7 5 7-5" fill="#fff" stroke="#1766b0" stroke-width="1"/></svg>
          <span>mathis.deloraux@quorlan-advisory.example</span>
        </li>
        <li class="contact__item">
          <svg class="contact__icon" viewBox="0 0 14 14" aria-hidden="true"><path d="M3.5 0h7v14h-7z M5 2v9h4V2z" fill-rule="evenodd"/></svg>
          <span>+33(0)6 28 40 13 85</span>
        </li>
        <li class="contact__item">
          <svg class="contact__icon" viewBox="0 0 14 14" aria-hidden="true"><path d="M3 0l3 3-1.5 2a9 9 0 0 0 4.5 4.5L11 8l3 3-2 3C6 13 1 8 0 2z"/></svg>
          <span>+33(0)4 71 86 52 09</span>
        </li>
      </ul>
      <span class="band__dot"></span>
    </section>
  </article>
</main>
</body>
</html>
```